Vemtri Gymnastics Silver gym banner

We need a banner for our new gym.
It should have navy, light blue, lilac and purple colors with our name, logo and other wording in navy color. Colors should bleed one into the other.
File with name, logo and other wording is attached.
Words: Rhythmic gymnastics, ballet, etc should be on the bottom

Target Market(s)

Girls 3 to 16 years of age

Industry/Entity Type

Athletics

Font styles to use
Other font styles liked:
• Please use fonts on file included

Colors
0054AA
0677BA
7BADD7
CADEEF
E8F1F8
0094D4
00A9DD
6FCCEA
C7EBF8
E9F6FB
00AB8E
00BBA5
67D7C9
C6EFE9
E9F9F6
6B429C
8869AF
B7A5CE
E3DAEB
F3F0F8

Requirements
Must have
• our logo and name of the gym
Nice to have
• rhythmic gymnastics feel
Should not have
• bold colors

```html
<!DOCTYPE html>
<html lang="en">
<head>
<meta charset="utf-8">
<title>Vemtri Gymnastics – School of Champions Banner</title>
<link rel="stylesheet" href="https://fonts.googleapis.com/css2?family=Lora:wght@600;700&family=Courgette&display=swap">
<style>
  :root {
    --page-bg: #e4e4e6;
    --paper: #ffffff;
    --navy: #1f3f9e;
    --ink: #2b2b2b;
    --band: #4d4f9e;
    --violet-deep: #2f3d8c;
    --violet-mid: #4a4c9f;
    --violet-light: #6a5cb6;
    --lilac: #a987e2;
    --bullet: #5553a6;
    --white: #ffffff;
  }
  html, body {
    margin: 0;
    padding: 0;
    width: 957px;
    height: 1200px;
    overflow: hidden;
    background: var(--page-bg);
  }
  .banner {
    position: absolute;
    left: 28px;
    top: 375px;
    width: 900px;
    height: 449px;
    background: var(--paper);
    overflow: hidden;
    box-shadow: 0 10px 24px rgba(0,0,0,0.22);
    font-family: "Lora", Georgia, serif;
  }
  .banner-shapes {
    position: absolute;
    inset: 0;
  }
  .brand {
    position: absolute;
    left: 50px;
    top: 22px;
    display: flex;
    align-items: center;
    gap: 14px;
  }
  .brand-name {
    font-size: 27px;
    font-weight: 600;
    color: var(--navy);
    white-space: nowrap;
  }
  .brand-dot {
    width: 54px;
    height: 54px;
    border-radius: 50%;
    background: var(--navy);
  }
  .program-list {
    position: absolute;
    left: 52px;
    top: 120px;
    margin: 0;
    padding: 0;
    list-style: none;
  }
  .program {
    position: relative;
    padding-left: 49px;
    font-size: 26px;
    font-weight: 700;
    line-height: 34px;
    color: var(--ink);
    margin-bottom: 5px;
  }
  .program .bullet {
    position: absolute;
    left: 0;
    top: 7px;
    width: 17px;
    height: 17px;
  }
  .program.two-line { width: 160px; }
  .web-address {
    position: absolute;
    left: 46px;
    top: 392px;
    display: flex;
    align-items: center;
    gap: 14px;
    color: var(--white);
    font-size: 26px;
    font-weight: 600;
    letter-spacing: 2.4px;
  }
  .web-address svg { width: 30px; height: 30px; }
  .gymnasts-photo {
    position: absolute;
    left: 400px;
    top: 170px;
    width: 500px;
    height: 279px;
    background:
      radial-gradient(ellipse 22% 50% at 72% 58%, rgba(214,170,130,0.75), transparent 70%),
      radial-gradient(ellipse 18% 42% at 45% 72%, rgba(200,160,130,0.65), transparent 70%),
      radial-gradient(ellipse 16% 40% at 92% 62%, rgba(120,190,220,0.6), transparent 70%),
      radial-gradient(ellipse 40% 18% at 50% 45%, rgba(169,135,226,0.45), transparent 70%);
  }
  .headline {
    position: absolute;
    left: 468px;
    top: 8px;
    color: var(--white);
  }
  .headline-main {
    display: block;
    font-family: "Lora", Georgia, serif;
    font-weight: 700;
    font-size: 78px;
    line-height: 90px;
    letter-spacing: 1px;
  }
  .headline-script {
    display: block;
    margin-left: -4px;
    margin-top: -16px;
    font-family: "Courgette", cursive;
    font-size: 52px;
    line-height: 64px;
    transform: rotate(-2deg);
    transform-origin: left center;
  }
</style>
</head>
<body>
  <div class="banner">
    <svg class="banner-shapes" viewBox="0 0 900 449" width="900" height="449" aria-hidden="true">
      <defs>
        <linearGradient id="violetField" x1="0" y1="0" x2="1" y2="0.3">
          <stop offset="0" stop-color="#2f3d8c"/>
          <stop offset="0.55" stop-color="#4a4c9f"/>
          <stop offset="1" stop-color="#6a5cb6"/>
        </linearGradient>
      </defs>
      <rect class="footer-band" x="0" y="377" width="900" height="72" fill="#4d4f9e"/>
      <path class="edge-lilac" transform="translate(-14,0)"
            d="M442,0 C380,60 362,170 420,262 C470,332 545,382 590,449 L900,449 L900,0 Z" fill="#a987e2"/>
      <path class="edge-white" transform="translate(-6,0)"
            d="M442,0 C380,60 362,170 420,262 C470,332 545,382 590,449 L900,449 L900,0 Z" fill="#ffffff"/>
      <path class="violet-field"
            d="M442,0 C380,60 362,170 420,262 C470,332 545,382 590,449 L900,449 L900,0 Z" fill="url(#violetField)"/>
    </svg>

    <div class="gymnasts-photo" role="img" aria-label="Photo of three rhythmic gymnasts performing with ribbons and a ball"></div>

    <div class="brand">
      <span class="brand-name">Vemtri Gymnastics</span>
      <span class="brand-dot"></span>
    </div>

    <ul class="program-list">
      <li class="program two-line"><svg class="bullet" viewBox="0 0 20 20"><circle cx="10" cy="10" r="10" fill="#5553a6"/><path d="M5 10h9M10.5 6.5 14 10l-3.5 3.5" stroke="#fff" stroke-width="2" fill="none" stroke-linecap="round"/></svg>Rhythmic Gymnastics</li>
      <li class="program"><svg class="bullet" viewBox="0 0 20 20"><circle cx="10" cy="10" r="10" fill="#5553a6"/><path d="M5 10h9M10.5 6.5 14 10l-3.5 3.5" stroke="#fff" stroke-width="2" fill="none" stroke-linecap="round"/></svg>Ballroom Dance</li>
      <li class="program"><svg class="bullet" viewBox="0 0 20 20"><circle cx="10" cy="10" r="10" fill="#5553a6"/><path d="M5 10h9M10.5 6.5 14 10l-3.5 3.5" stroke="#fff" stroke-width="2" fill="none" stroke-linecap="round"/></svg>Ballet</li>
      <li class="program"><svg class="bullet" viewBox="0 0 20 20"><circle cx="10" cy="10" r="10" fill="#5553a6"/><path d="M5 10h9M10.5 6.5 14 10l-3.5 3.5" stroke="#fff" stroke-width="2" fill="none" stroke-linecap="round"/></svg>Stretching</li>
      <li class="program"><svg class="bullet" viewBox="0 0 20 20"><circle cx="10" cy="10" r="10" fill="#5553a6"/><path d="M5 10h9M10.5 6.5 14 10l-3.5 3.5" stroke="#fff" stroke-width="2" fill="none" stroke-linecap="round"/></svg>Hip Hop</li>
    </ul>

    <div class="web-address">
      <svg viewBox="0 0 30 30" aria-hidden="true">
        <g fill="none" stroke="#fff" stroke-width="1.6">
          <circle cx="15" cy="15" r="12"/>
          <ellipse cx="15" cy="15" rx="5" ry="12"/>
          <path d="M3 15h24M5 9h20M5 21h20"/>
        </g>
      </svg>
      <span>www.vemtrigymnastics.com</span>
    </div>

    <h1 class="headline" style="margin:0;font-weight:normal;">
      <span class="headline-main">School of</span>
      <span class="headline-script">Champions</span>
    </h1>
  </div>
</body>
</html>
```